Create branded design templates/backgrounds for social media based on UK property investing company

I'd like Instagram, Facebook and Linkedin backgrounds/templates to add text to, based on my logo design and business of UK holiday let investing. Ideally I'd have some base designs for me to approve, then engage with the winning designer further to create about 50 different templates. I looking for a mixture of templates with the logo and using logo colours, others of internal holiday let photos including logos and a few of my photo imposed on the front of them.

Target Market(s)

Middle aged adults

Industry/Entity Type

Holiday let properties

Requirements
Must have
• a distinct brand look that can be replicated

```html
<!DOCTYPE html>
<html lang="en">
<head>
<meta charset="utf-8">
<title>Harbourline Homes – Build Your Portfolio</title>
<link href="https://fonts.googleapis.com/css2?family=Montserrat:wght@300;400;500;700;800;900&display=swap" rel="stylesheet">
<style>
  :root {
    --brand-blue: #0786d0;
    --brand-green: #5aab0b;
    --brand-yellow: #f7d92c;
    --ink-dark: #2e2e2e;
    --ink-grey: #4a4a4a;
    --white: #ffffff;
  }
  * { margin: 0; padding: 0; box-sizing: border-box; }
  html, body { width: 1200px; height: 1200px; overflow: hidden; background: var(--white); }
  body { font-family: "Montserrat", sans-serif; }

  .poster { position: relative; width: 1200px; height: 1200px; overflow: hidden; }

  .street-photo {
    position: absolute; inset: 0;
    background:
      radial-gradient(circle at 78% 8%, rgba(255,236,190,0.95) 0%, rgba(255,225,170,0.4) 18%, rgba(255,225,170,0) 40%),
      linear-gradient(180deg, #b8795a 0%, #c88f6a 25%, #d9c3a5 50%, #b9ad98 70%, #8f8d86 100%);
  }
  .consultant-photo {
    position: absolute; left: 714px; top: 404px; width: 486px; height: 593px;
    background: linear-gradient(180deg, #d8c4ad 0%, #c9b3a0 30%, #8a8f86 60%, #5a6258 100%);
  }

  .shapes { position: absolute; inset: 0; }

  .brand-card {
    position: absolute; left: 32px; top: 0; width: 470px; height: 159px;
    background: var(--white); border-radius: 0 0 62px 62px;
    display: flex; align-items: center; gap: 18px; padding-left: 48px;
  }
  .brand-mark { width: 40px; height: 40px; background: var(--brand-blue); flex: none; }
  .brand-name { font-weight: 500; font-size: 34px; color: var(--ink-grey); letter-spacing: 0.5px; }

  .tagline {
    position: absolute; left: 83px; top: 380px;
    font-size: 38px; font-weight: 300; color: var(--white); letter-spacing: -0.3px;
  }
  .tagline strong { font-weight: 800; color: var(--brand-blue); }

  .headline {
    position: absolute; left: 82px; top: 470px; width: 600px;
    font-size: 82px; font-weight: 800; line-height: 77px; color: var(--brand-blue); letter-spacing: -2.3px;
  }

  .intro {
    position: absolute; left: 84px; top: 852px; width: 520px;
    font-size: 31.5px; font-weight: 300; line-height: 32px; color: var(--brand-blue); letter-spacing: -0.5px;
  }

  .contact-heading {
    position: absolute; right: 544px; top: 1050px;
    font-size: 52px; font-weight: 900; line-height: 50px; color: var(--ink-dark);
    text-align: right; letter-spacing: -1.5px;
  }
  .contact-icons { position: absolute; left: 676px; top: 1054px; }

  .contact-phone {
    position: absolute; left: 766px; top: 1052px;
    font-size: 53px; font-weight: 800; color: var(--brand-blue); letter-spacing: -0.5px; line-height: 56px;
  }
  .contact-email {
    position: absolute; left: 748px; top: 1112px;
    font-size: 28px; font-weight: 500; color: var(--brand-blue); line-height: 36px;
  }
</style>
</head>
<body>
<main class="poster">
  <div class="street-photo" role="img" aria-label="Photo of a row of sunlit detached houses with terracotta tiled roofs"></div>

  <svg class="shapes" width="1200" height="1200" viewBox="0 0 1200 1200" aria-hidden="true">
    <path d="M502 75 H1087 Q1112 75 1112 100 V997" fill="none" stroke="var(--brand-blue)" stroke-width="4"/>
    <path d="M85 150 V230" fill="none" stroke="var(--brand-blue)" stroke-width="4"/>
    <path d="M0 219 H600 Q640 219 660 260 V282 H0 Z" fill="var(--brand-blue)"/>
    <path d="M0 251 H650 Q675 251 690 282 V300 H0 Z" fill="var(--brand-green)"/>
    <path d="M0 282 H656 Q714 282 714 340 V1112 H0 Z" fill="var(--brand-yellow)"/>
  </svg>

  <div class="consultant-photo" role="img" aria-label="Portrait photo of the company consultant standing in front of the houses"></div>

  <svg class="shapes" width="1200" height="1200" viewBox="0 0 1200 1200" aria-hidden="true">
    <path d="M0 1112 H407 C425 1040 478 997 560 997 H1200 V1200 H0 Z" fill="var(--white)"/>
    <path d="M87 1108 Q100 1124 120 1124 H405" fill="none" stroke="var(--brand-blue)" stroke-width="4"/>
  </svg>

  <header class="brand-card">
    <span class="brand-mark"></span>
    <span class="brand-name">Harbourline Homes</span>
  </header>

  <p class="tagline">Invest In <strong>YOUR</strong> Future</p>

  <h1 class="headline">Build Your portfolio of Property prosperity</h1>

  <p class="intro">Get in contact with us and we will advice, consult and create a perfectly tailored plan for you to invest and maximise your ROI.</p>

  <h2 class="contact-heading">GET IN<br>TOUCH</h2>

  <svg class="contact-icons" width="46" height="92" viewBox="0 0 46 92" aria-hidden="true">
    <path d="M6 4 L15 2 L21 15 L15 20 C18 27 22 31 28 34 L33 28 L45 34 L43 43 C30 46 4 22 6 4 Z" fill="var(--brand-green)"/>
    <rect x="1" y="58" width="43" height="31" rx="3" fill="var(--brand-green)"/>
    <path d="M3 61 L22.5 76 L42 61" fill="none" stroke="var(--white)" stroke-width="3"/>
  </svg>

  <p class="contact-phone">+286 5550 142</p>
  <p class="contact-email">info@harbourlinehomes.uk</p>
</main>
</body>
</html>
```